Online Dating Website called WinkAtWheel.com

PLEASE CAN ALL PARTICIPATING DESIGNERS PLEASE SUBMIT ALL PAGES AS DETAILED IN THE ORIGINAL BRIEF BELOW WITHIN 48 HOURS TO AVOID WINKATWHEEL EXTENDING THE CONTEST FURTHER.

We have an online dating website that is 95% fully functional and now require an exciting and creative designer to help us create the best dating experience. We are looking for your ideas on a couple of our key pages. These are our landing, profile and search page. We already have a homepage that we are happy with and winning designers will look to build upon the foundations of the homepage and extend them through their designs.

The premise of the site is the idea that if you've ever seen someone out driving and wished you could communicate because you found them attractive, how would you? Well with WinkAtWheel.com you can. Just enter their vehicle registration number (license plate) in to the website in order to get in touch, flirt and develop a relationship. It also allows users to find each other based on other criteria. It acts as both a specialist service and a normal dating website.

The pages that require developing are 1) our landing page, this is the page users see when they first login to the site, it comprises various pieces of information but it's primary function is a live feed of events generated based on the users favourited profiles and interactions with the user. 2) The profile page is the page where users can edit their own information, given the nature of this page we are looking for a creative design that gives this page some flair. 3) Finally we are looking for ideas for our search page, this page needs to provide a list of users who meet the user's search requirements and display the profile of a selected user.

Reason: We've asked for certain pages in our brief to be designed and this still hasn't been done. We've contacted the designers that have currently submitted designs and requested this several times. We still await for this to happen.

Target Market(s)

Male or Female age 18+

Industry/Entity Type

Dating

Requirements
Must have
• Our must have feature is a designer with an open mind. The functionality of the site must be present, all we ask is for you to be creative with the layout. Think out side of the box, change the colours, the layout, and the background as you feel. Make it look current and appealing to the user.
Nice to have
• Theme's carried through from the home page
Should not have
• Do not include Comic Sans or Times New Roman font in your designs.

```html
<!DOCTYPE html>
<html lang="en">
<head>
<meta charset="utf-8">
<title>WinkAtWheel.com – Home</title>
<link rel="stylesheet" href="https://fonts.googleapis.com/css2?family=Ubuntu:wght@300;400;500&family=Open+Sans:wght@400;600&display=swap">
<style>
  :root {
    --canvas: #e6e6e6;
    --page: #ffffff;
    --red: #e2474f;
    --ink: #333333;
    --muted: #7a7a7a;
    --strip: #353535;
    --strip-dark: #252525;
    --footer: #2a2a2a;
    --footer-text: #9a9a9a;
    --line: #dddddd;
    --online: #5bc35b;
  }
  * { box-sizing: border-box; margin: 0; padding: 0; }
  html, body { width: 826px; height: 1200px; overflow: hidden; }
  body { background: var(--canvas); font-family: "Open Sans", sans-serif; color: var(--ink); position: relative; }

  .page { position: absolute; left: 33px; top: 0; width: 760px; height: 1110px; background: var(--page); }

  .logo { position: absolute; left: 12px; top: 38px; width: 222px; height: 68px;
    background: linear-gradient(#dcdcdc, #c9c9c9); display: flex; align-items: flex-end; padding: 0 0 14px 12px; }
  .logo span { font-family: "Ubuntu", sans-serif; font-size: 13px; font-weight: 500; color: #3c3c3c; }

  .account-links { position: absolute; right: 12px; font-family: "Ubuntu", sans-serif; font-size: 9px; color: var(--muted); letter-spacing: .3px; }
  .account-links.primary { top: 14px; }
  .account-links.secondary { top: 48px; }
  .account-links span + span::before { content: "|"; margin: 0 7px; color: #bbb; }

  .main-nav { position: absolute; left: 0; top: 168px; width: 760px; height: 56px; background: var(--red);
    display: flex; align-items: center; }
  .main-nav a { font-family: "Ubuntu", sans-serif; font-size: 17px; color: #fff; text-decoration: none; text-transform: uppercase; margin-left: 72px; }
  .main-nav a:first-child { margin-left: 52px; }

  .hero { position: absolute; left: 0; top: 224px; width: 760px; height: 280px;
    background: radial-gradient(ellipse at 62% 45%, #d9a57a 0%, #a86b45 28%, #5a3a2a 60%, #2a1d18 100%); }

  .quick-search { position: absolute; left: 27px; top: 22px; width: 245px; height: 226px; background: rgba(35,35,35,.72); }
  .quick-search .tag { position: absolute; left: 0; top: -13px; font-size: 8px; color: #ddd; background: rgba(35,35,35,.72); padding: 2px 6px; font-family: "Ubuntu", sans-serif; }
  .quick-search .title { position: absolute; left: -38px; top: 100px; transform: rotate(-90deg); font-family: "Ubuntu", sans-serif;
    font-size: 17px; letter-spacing: 1px; color: #f2f2f2; white-space: nowrap; }
  .quick-search .title b { color: var(--red); font-weight: 400; }
  .qs-label { position: absolute; font-size: 9px; color: #eee; }
  .qs-field { position: absolute; height: 15px; background: #fff; }
  .qs-field::after { content: ""; position: absolute; right: 4px; top: 5px; border: 3px solid transparent; border-top-color: #555; }
  .qs-field.text::after { display: none; }
  .qs-go { position: absolute; left: 185px; top: 128px; width: 50px; height: 36px; background: var(--red); color: #fff;
    font-family: "Ubuntu", sans-serif; font-size: 13px; display: flex; align-items: center; justify-content: center; }

  .slider-dots { position: absolute; right: 14px; bottom: 12px; display: flex; gap: 5px; }
  .slider-dots i { width: 8px; height: 8px; border-radius: 50%; background: #888; }
  .slider-dots i.on { background: var(--red); }

  .members { position: absolute; left: 0; top: 504px; width: 760px; height: 152px; background: var(--strip); }
  .member-tabs { position: absolute; left: 14px; top: 0; display: flex; }
  .member-tabs span { font-family: "Ubuntu", sans-serif; font-size: 9px; color: #ccc; padding: 5px 14px; background: #444; margin-right: 2px; text-transform: uppercase; height: 28px; }
  .member-tabs span.active { background: var(--strip-dark); color: #fff; }
  .member-tabs span.active b { display: block; color: var(--online); font-weight: 400; font-size: 8px; }
  .member-row { position: absolute; left: 52px; top: 42px; display: flex; gap: 17px; }
  .member { width: 66px; }
  .member .photo { width: 66px; height: 70px; border: 2px solid #fff; background: linear-gradient(160deg, #8a7566, #3f342e); }
  .member .hearts { margin-top: 5px; display: flex; justify-content: center; gap: 3px; }
  .member .hearts svg { width: 8px; height: 8px; }
  .member-arrow { position: absolute; top: 64px; }

  .column { position: absolute; top: 690px; width: 230px; height: 380px; }
  .column h2 { font-family: "Ubuntu", sans-serif; font-weight: 300; font-size: 22px; color: var(--red); padding-bottom: 10px; border-bottom: 1px solid var(--line); }
  .column p { font-size: 10.5px; line-height: 17px; color: #444; margin-top: 14px; }
  .column .more { position: absolute; right: 0; bottom: 0; font-size: 10px; color: #999; }
  .col-welcome { left: 12px; }
  .col-stories { left: 265px; }
  .col-sexy { left: 518px; }
  .story-head { display: flex; gap: 10px; margin-top: 12px; }
  .story-head .photo { width: 62px; height: 62px; background: linear-gradient(150deg, #b58a6a, #4b3428); flex: none; }
  .story-head .names { font-family: "Ubuntu", sans-serif; font-size: 12px; color: #444; margin-top: 6px; }
  .story-head .names b { color: var(--red); font-weight: 400; }
  .story-head .date { font-size: 8px; color: var(--muted); }
  .col-stories p { margin-top: 8px; }

  .site-footer { position: absolute; left: 0; top: 1110px; width: 826px; height: 90px; background: var(--footer); }
  .footer-col { position: absolute; top: 12px; width: 160px; }
  .footer-col h3 { font-family: "Ubuntu", sans-serif; font-size: 11px; font-weight: 400; color: #fff; margin-bottom: 4px; }
  .footer-col li { list-style: none; font-size: 7px; line-height: 11px; color: var(--footer-text); }
  .footer-col li:first-child { color: #e0e0e0; }
  .copyright { position: absolute; left: 0; right: 0; bottom: 4px; text-align: center; font-size: 7px; color: #777; }
</style>
</head>
<body>
  <div class="page">
    <header>
      <div class="logo"><span>WinkAtWheel.com</span></div>
      <nav class="account-links primary"><span>HI, USER</span><span>MY ACCOUNT</span><span>PRIVACY SETTINGS</span><span>HELP</span><span>SIGN OUT</span></nav>
      <nav class="account-links secondary"><span>NEW MESSAGES (1)</span><span>ACTIVITY</span><span>PHOTO REQUESTS</span><span>FRIENDS</span></nav>
    </header>

    <nav class="main-nav">
      <a href="#">My Zone</a><a href="#">Gallery</a><a href="#">Shopping</a><a href="#">Tips</a><a href="#">Contact Us</a>
    </nav>

    <section class="hero" role="img" aria-label="Photo of a couple embracing">
      <form class="quick-search">
        <span class="tag">ADVANCED SEARCH</span>
        <div class="title">QUICK <b>SEARCH</b></div>
        <span class="qs-label" style="left:42px;top:61px">I am</span>
        <span class="qs-field" style="left:65px;top:59px;width:55px"></span>
        <span class="qs-label" style="left:128px;top:61px">Looking For</span>
        <span class="qs-field" style="left:185px;top:59px;width:50px"></span>
        <span class="qs-label" style="left:42px;top:96px">Age</span>
        <span class="qs-field" style="left:65px;top:94px;width:55px"></span>
        <span class="qs-label" style="left:145px;top:96px">to</span>
        <span class="qs-field" style="left:185px;top:94px;width:50px"></span>
        <span class="qs-label" style="left:42px;top:140px">Email</span>
        <span class="qs-field text" style="left:70px;top:138px;width:100px"></span>
        <span class="qs-go">Go</span>
      </form>
      <div class="slider-dots"><i class="on"></i><i></i><i></i><i></i></div>
    </section>

    <section class="members">
      <div class="member-tabs">
        <span class="active">Online<b>310</b></span><span>New Guys</span><span>Couples</span>
      </div>
      <svg class="member-arrow" style="left:16px" width="14" height="24" viewBox="0 0 14 24"><path d="M11 2 2 12l9 10" fill="none" stroke="#aaa" stroke-width="2"/></svg>
      <svg class="member-arrow" style="right:16px" width="14" height="24" viewBox="0 0 14 24"><path d="M3 2l9 10-9 10" fill="none" stroke="#aaa" stroke-width="2"/></svg>
      <div class="member-row">
        <div class="member"><div class="photo" role="img" aria-label="Member photo"></div><div class="hearts"><svg viewBox="0 0 10 9"><path d="M5 9 0 4a2.5 2.5 0 0 1 5-3 2.5 2.5 0 0 1 5 3z" fill="#e2474f"/></svg><svg viewBox="0 0 10 9"><path d="M5 9 0 4a2.5 2.5 0 0 1 5-3 2.5 2.5 0 0 1 5 3z" fill="#e2474f"/></svg><svg viewBox="0 0 10 9"><path d="M5 9 0 4a2.5 2.5 0 0 1 5-3 2.5 2.5 0 0 1 5 3z" fill="#777"/></svg></div></div>
        <div class="member"><div class="photo" role="img" aria-label="Member photo"></div><div class="hearts"><svg viewBox="0 0 10 9"><path d="M5 9 0 4a2.5 2.5 0 0 1 5-3 2.5 2.5 0 0 1 5 3z" fill="#e2474f"/></svg><svg viewBox="0 0 10 9"><path d="M5 9 0 4a2.5 2.5 0 0 1 5-3 2.5 2.5 0 0 1 5 3z" fill="#e2474f"/></svg><svg viewBox="0 0 10 9"><path d="M5 9 0 4a2.5 2.5 0 0 1 5-3 2.5 2.5 0 0 1 5 3z" fill="#777"/></svg></div></div>
        <div class="member"><div class="photo" role="img" aria-label="Member photo"></div><div class="hearts"><svg viewBox="0 0 10 9"><path d="M5 9 0 4a2.5 2.5 0 0 1 5-3 2.5 2.5 0 0 1 5 3z" fill="#e2474f"/></svg><svg viewBox="0 0 10 9"><path d="M5 9 0 4a2.5 2.5 0 0 1 5-3 2.5 2.5 0 0 1 5 3z" fill="#e2474f"/></svg><svg viewBox="0 0 10 9"><path d="M5 9 0 4a2.5 2.5 0 0 1 5-3 2.5 2.5 0 0 1 5 3z" fill="#777"/></svg></div></div>
        <div class="member"><div class="photo" role="img" aria-label="Member photo"></div><div class="hearts"><svg viewBox="0 0 10 9"><path d="M5 9 0 4a2.5 2.5 0 0 1 5-3 2.5 2.5 0 0 1 5 3z" fill="#e2474f"/></svg><svg viewBox="0 0 10 9"><path d="M5 9 0 4a2.5 2.5 0 0 1 5-3 2.5 2.5 0 0 1 5 3z" fill="#e2474f"/></svg><svg viewBox="0 0 10 9"><path d="M5 9 0 4a2.5 2.5 0 0 1 5-3 2.5 2.5 0 0 1 5 3z" fill="#777"/></svg></div></div>
        <div class="member"><div class="photo" role="img" aria-label="Member photo"></div><div class="hearts"><svg viewBox="0 0 10 9"><path d="M5 9 0 4a2.5 2.5 0 0 1 5-3 2.5 2.5 0 0 1 5 3z" fill="#e2474f"/></svg><svg viewBox="0 0 10 9"><path d="M5 9 0 4a2.5 2.5 0 0 1 5-3 2.5 2.5 0 0 1 5 3z" fill="#e2474f"/></svg><svg viewBox="0 0 10 9"><path d="M5 9 0 4a2.5 2.5 0 0 1 5-3 2.5 2.5 0 0 1 5 3z" fill="#777"/></svg></div></div>
        <div class="member"><div class="photo" role="img" aria-label="Member photo"></div><div class="hearts"><svg viewBox="0 0 10 9"><path d="M5 9 0 4a2.5 2.5 0 0 1 5-3 2.5 2.5 0 0 1 5 3z" fill="#e2474f"/></svg><svg viewBox="0 0 10 9"><path d="M5 9 0 4a2.5 2.5 0 0 1 5-3 2.5 2.5 0 0 1 5 3z" fill="#e2474f"/></svg><svg viewBox="0 0 10 9"><path d="M5 9 0 4a2.5 2.5 0 0 1 5-3 2.5 2.5 0 0 1 5 3z" fill="#777"/></svg></div></div>
        <div class="member"><div class="photo" role="img" aria-label="Member photo"></div><div class="hearts"><svg viewBox="0 0 10 9"><path d="M5 9 0 4a2.5 2.5 0 0 1 5-3 2.5 2.5 0 0 1 5 3z" fill="#e2474f"/></svg><svg viewBox="0 0 10 9"><path d="M5 9 0 4a2.5 2.5 0 0 1 5-3 2.5 2.5 0 0 1 5 3z" fill="#e2474f"/></svg><svg viewBox="0 0 10 9"><path d="M5 9 0 4a2.5 2.5 0 0 1 5-3 2.5 2.5 0 0 1 5 3z" fill="#777"/></svg></div></div>
        <div class="member"><div class="photo" role="img" aria-label="Member photo"></div><div class="hearts"><svg viewBox="0 0 10 9"><path d="M5 9 0 4a2.5 2.5 0 0 1 5-3 2.5 2.5 0 0 1 5 3z" fill="#e2474f"/></svg><svg viewBox="0 0 10 9"><path d="M5 9 0 4a2.5 2.5 0 0 1 5-3 2.5 2.5 0 0 1 5 3z" fill="#e2474f"/></svg><svg viewBox="0 0 10 9"><path d="M5 9 0 4a2.5 2.5 0 0 1 5-3 2.5 2.5 0 0 1 5 3z" fill="#777"/></svg></div></div>
      </div>
    </section>

    <section class="column col-welcome">
      <h2>WELCOME</h2>
      <p>Lorem Ipsum is simply dummy text of the printing and typesetting industry. Lorem Ipsum has been the industry's standard dummy text ever since the 1500s, when an unknown printer took a galley of type and scrambled it to make a type specimen book. It has survived not only five centuries, but also the leap into electronic typesetting, remaining essentially unchanged. It was popularised in the 1960s with the release of tronic.y five centuries, but also the leap with the release of tronic.</p>
      <span class="more">›</span>
    </section>

    <section class="column col-stories">
      <h2>SUCESS STORIES</h2>
      <div class="story-head">
        <div class="photo" role="img" aria-label="Photo of a happy couple"></div>
        <div>
          <div class="names">MARISA <b>♥</b> DYLAN</div>
          <div class="date">Dating Started 25 Oct 2013</div>
        </div>
      </div>
      <p>Leo, but also the leap into electronic typesetting, remaining essentially unchanged. It was popularised in the 1960s with the release of tronic.y five centuries, but also the leap with the release of tronic.Leo, but also the leap into electronic typesettingchanged. It was popularised in the 1960s</p>
      <span class="more">›</span>
    </section>

    <section class="column col-sexy">
      <h2>BE MORE SEXY</h2>
      <p>Lorem Ipsum is simply dummy text of the printing and typesetting industry. Lorem Ipsum has been the industry's standard dummy text ever since the 1500s, when an unknown printer took a galley of type and scrambled it to make a type specimen book. It has survived not only five centuries, but also the leap into electronic typesetting, remaining essentially unchanged. It was popularised in the 1960s with the release of tronic.y five centuries, but also the leap with the release of tronic.</p>
      <span class="more">›</span>
    </section>
  </div>

  <footer class="site-footer">
    <div class="footer-col" style="left:70px"><h3>QUICK LINKS</h3><ul><li>Full Service Solution</li><li>Lead Pilot</li><li>Onsite Help</li><li>Group Offers</li><li>Data Plans</li></ul></div>
    <div class="footer-col" style="left:250px"><h3>FOLLOW US</h3><ul><li>Full Service Solution</li><li>Lead Pilot</li><li>Onsite Help</li><li>Group Offers</li><li>Data Plans</li></ul></div>
    <div class="footer-col" style="left:440px"><h3>SERVICES</h3><ul><li>Full Service Solution</li><li>Lead Pilot</li><li>Onsite Help</li><li>Group Offers</li><li>Data Plans</li></ul></div>
    <div class="footer-col" style="left:615px"><h3>CONTACT</h3><ul><li>Full Service Solution</li><li>Lead Pilot</li><li>Onsite Help</li><li>Group Offers</li><li>Data Plans</li></ul></div>
    <div class="copyright">Copyright © winkatwheel.com All rights reserved</div>
  </footer>
</body>
</html>
```